Brochure Design Project

We are a payroll company. We offer a wide variety of products and services:
1. Payroll Processing
2. Employee Direct Deposit
3. Time and attendance
4. HR services
5. Employee Employee Benefits

I'd like to develop a one page template that uses a combination of our logo (attached), colors (attached) and possible a picture. The picture could be shown as an option as it may change based on the product or service.

Target Market(s)

Adults in the United States ages 22-50. Typically these people are accountants, human resource professionals or entrepreneurs. The payroll industry is dominated by 3 large payroll processors, KLV, Wendorn and Tolvaris. These companies are very impersonal and make it difficult to resolve issues when they arise. We have grown to over 400 clients by being the opposite of the big guys,

Industry/Entity Type

It Company

Font styles to use
Sans Serif

Requirements
Must have
• The brochure can be one or two pages.
Nice to have
• I'll know it when I see it but I can't describe it. I have attached a few brochures that have caught my eye.
Should not have
• No cartoons. No money signs. Hip, new, fresh are words I'd use to describe the winning product. Of the three people I described in my target market, the entrepreneur is the market I'd most like to target.

```html
<!DOCTYPE html>
<html lang="en">
<head>
<meta charset="utf-8">
<title>Paydesk Partners – HR and Time &amp; Attendance</title>
<link rel="stylesheet" href="https://fonts.googleapis.com/css2?family=Noto+Sans:wght@400;700&family=Noto+Serif:wght@500;700&display=swap">
<style>
  :root {
    --navy: #1b2f6b;
    --heading-blue: #173f86;
    --text: #2b2b2b;
    --green: #8cc63f;
    --grey-band: #6f6f71;
    --divider: #9a9a9a;
    --paper: #ffffff;
    --photo-light: #e9edf1;
    --photo-mid: #9aa6b3;
  }
  * { margin: 0; padding: 0; box-sizing: border-box; }
  html, body { width: 849px; height: 1200px; overflow: hidden; background: var(--paper); }
  .brochure {
    position: relative; width: 849px; height: 1200px; overflow: hidden;
    font-family: "Noto Sans", Arial, sans-serif; color: var(--text);
    font-size: 14px; line-height: 1.3;
  }
  .hero { position: absolute; top: 0; left: 0; width: 849px; height: 400px; }
  .column { position: absolute; top: 0; }
  .column--hr { left: 46px; width: 362px; top: 412px; }
  .column--time { left: 467px; width: 352px; top: 344px; }
  .divider { position: absolute; left: 434px; top: 332px; width: 1px; height: 742px; background: var(--divider); }
  .section-title {
    font-family: "Noto Serif", Georgia, serif; font-weight: 500; color: var(--navy);
    font-size: 28px; letter-spacing: 0.5px; text-align: center; margin-bottom: 16px;
  }
  .intro { margin-bottom: 20px; }
  .service { margin-bottom: 18px; }
  .service-name, .feature-title {
    font-weight: 700; color: var(--heading-blue); font-size: 14.5px;
  }
  .feature-title { font-size: 15px; margin: 0 0 12px; }
  .feature-list { list-style: none; margin-bottom: 22px; }
  .feature-list li { position: relative; padding-left: 20px; margin-bottom: 2px; }
  .feature-list li::before { content: "•"; position: absolute; left: 4px; }
  .brand {
    position: absolute; left: 590px; top: 920px; width: 220px;
    font-family: "Noto Sans", Arial, sans-serif; font-weight: 700; color: var(--navy);
    font-size: 30px; line-height: 1.05; text-align: center;
  }
  .footer-band { position: absolute; left: 0; top: 980px; width: 849px; height: 220px; }
  .contact {
    position: absolute; right: 40px; top: 1068px; text-align: right; color: var(--paper);
    font-family: "Noto Serif", Georgia, serif; font-weight: 700; font-size: 16px; line-height: 1.38;
  }
</style>
</head>
<body>
<main class="brochure">
  <svg class="hero" viewBox="0 0 849 400" aria-hidden="false">
    <defs>
      <linearGradient id="photoTone" x1="0" y1="0" x2="1" y2="1">
        <stop offset="0" stop-color="var(--photo-light)"/>
        <stop offset="0.6" stop-color="var(--photo-mid)"/>
        <stop offset="1" stop-color="#3b4150"/>
      </linearGradient>
    </defs>
    <rect width="849" height="400" fill="url(#photoTone)" role="img" aria-label="Photo of a business team meeting around a table with laptops and documents"/>
    <path d="M0 335 C 240 400, 520 270, 849 248 L849 400 L0 400 Z" fill="var(--green)"/>
    <path d="M0 372 C 250 420, 530 300, 849 282 L849 400 L0 400 Z" fill="var(--paper)"/>
  </svg>

  <div class="divider"></div>

  <section class="column column--hr">
    <h2 class="section-title">HUMAN RESOURCE</h2>
    <p class="intro">Paydesk Partners provides a customized approach and comprehensive set of HR Solutions for your business.<br>Our services are designed to help businesses minimize risk, save money, and eliminate the hassle of managing employee services.</p>
    <div class="service"><h3 class="service-name">Employee Screening</h3><p>Pre-employment screening, employee background checks, drug testing and more</p></div>
    <div class="service"><h3 class="service-name">New Hire Reporting</h3><p>Employer reporting for new hires that complies with federal and state laws requirements</p></div>
    <div class="service"><h3 class="service-name">Time &amp; Attendence</h3><p>Automated applications increase accountability, save time and money</p></div>
    <div class="service"><h3 class="service-name">Expense Tracking</h3><p>Integrated expense tracking &amp; reporting</p></div>
    <div class="service"><h3 class="service-name">Customized HR Reporting</h3><p>For increased business intelligence</p></div>
    <div class="service"><h3 class="service-name">Employee Communications</h3><p>For enhanced employee relations</p></div>
    <div class="service"><h3 class="service-name">Employee Self-Service Portal (ESP)</h3><p>The Self-Service Model saves employers time, effort and money while increasing employee satisfaction.</p></div>
  </section>

  <section class="column column--time">
    <h2 class="section-title">TIME &amp; ATTENDENCE</h2>
    <p class="intro">A comprehensive benefits administration program is important when it comes to hiring and retaining quality employees. Benefits Administration is a complex task and can be taxing on your staff. Paydesk Partners offers a seamless way to manage this for your business.</p>
    <h3 class="feature-title">Benefits Administration Features</h3>
    <ul class="feature-list">
      <li>24/7 Access &amp; reporting features of your companies data</li>
      <li>A dedicated benefits specialist to manage your program and provide superior customer care</li>
      <li>Easy integration with other services including Payroll Management and HR services</li>
    </ul>
    <h3 class="feature-title">Specific services we offer as part of our benefits administration offerings:</h3>
    <ul class="feature-list">
      <li>Healthcare Administration</li>
      <li>Flexible Spending Accounts</li>
      <li>Cobra Administration</li>
      <li>Retirement Services</li>
      <li>Leave Administration Services</li>
      <li>Carrier Enrollment Services</li>
      <li>Total Compensations Services</li>
      <li>Advocacy Services</li>
    </ul>
  </section>

  <div class="brand">Paydesk<br>Partners</div>

  <svg class="footer-band" viewBox="0 0 849 220" aria-hidden="true">
    <path d="M0 92 C 260 110, 560 40, 849 30 L849 220 L0 220 Z" fill="var(--grey-band)"/>
  </svg>

  <address class="contact">
    Paydesk Partners, Inc.<br>
    Call Phone: 555-014-2290<br>
    E-mail: hello@paydeskpartners.com<br>
    © 2014 Paydesk Associates Inc. All rights reserved.
  </address>
</main>
</body>
</html>
```